Professional business cards for real estate development company

I need business cards for my new real estate development company. The company, "LUMAR" is a real estate development, investment, and advisory firm with a focus on multifamily, office, and mixed-use projects across primary and secondary markets in the Southeast United States.

Style preference is modern

Industry/Entity Type

Real Estate Development

Contact Information for Business Card

The business cards need to include:
Name
Title
Mailing Address
Phone Number
Web Address

Logo is attached. I would like white to be the primary color with incorporation of the company colors: #232D3A and #B5A451

Font styles to use
Other font styles liked:
• Montserrat, Avenir

Requirements
Must have
• Company Logo. No need to include the company name since the name is in the logo.
Should not have
• No line type designs

```html
<!DOCTYPE html>
<html lang="en">
<head>
<meta charset="utf-8">
<title>LUMAR Business Card</title>
<link href="https://fonts.googleapis.com/css2?family=Open+Sans:wght@400;600;700&display=swap" rel="stylesheet">
<style>
  :root {
    --navy: #202b3a;
    --navy-soft: #34445a;
    --ink: #232d3a;
    --grey-text: #555b63;
    --paper: #ffffff;
    --backdrop: #9e9e9e;
  }
  html, body {
    margin: 0;
    padding: 0;
    width: 1049px;
    height: 1200px;
    overflow: hidden;
    background: var(--backdrop);
    font-family: "Open Sans", sans-serif;
  }
  .canvas {
    position: relative;
    width: 1049px;
    height: 1200px;
  }
  .card {
    position: absolute;
    left: 163px;
    width: 722px;
    border-radius: 24px;
    overflow: hidden;
  }
  .card--front {
    top: 139px;
    height: 411px;
    background: var(--navy);
    display: flex;
    align-items: center;
    justify-content: center;
  }
  .front-wordmark {
    display: flex;
    align-items: center;
    gap: 18px;
    font-weight: 600;
    font-size: 84px;
    letter-spacing: 2px;
    color: var(--navy-soft);
  }
  .front-wordmark .mark-square {
    width: 26px;
    height: 26px;
    background: var(--navy-soft);
  }
  .card--back {
    top: 646px;
    height: 413px;
    background: var(--paper);
  }
  .name-tab {
    position: absolute;
    left: 0;
    top: 183px;
    width: 13px;
    height: 48px;
    background: var(--ink);
    border-radius: 0 5px 5px 0;
  }
  .person {
    position: absolute;
    left: 37px;
    top: 178px;
  }
  .person-name {
    margin: 0;
    font-weight: 700;
    font-size: 27px;
    color: var(--ink);
    letter-spacing: 0.5px;
    line-height: 1.2;
  }
  .person-title {
    margin: 2px 0 0;
    font-size: 18px;
    color: var(--grey-text);
  }
  .brand {
    position: absolute;
    left: 409px;
    top: 96px;
    display: flex;
    align-items: center;
    gap: 12px;
    font-weight: 600;
    font-size: 56px;
    line-height: 1;
    color: var(--ink);
    letter-spacing: 1px;
  }
  .brand .mark-square {
    width: 18px;
    height: 18px;
    background: var(--ink);
  }
  .address {
    position: absolute;
    left: 409px;
    top: 219px;
    margin: 0;
    font-style: normal;
    font-size: 18.5px;
    line-height: 26px;
    color: var(--grey-text);
  }
  .contacts {
    position: absolute;
    left: 409px;
    top: 301px;
    margin: 0;
    padding: 0;
    list-style: none;
    font-size: 18.5px;
    line-height: 25px;
    color: var(--grey-text);
  }
  .contacts li {
    display: flex;
    align-items: center;
    gap: 5px;
  }
  .contacts svg {
    width: 15px;
    height: 15px;
    flex: none;
    fill: var(--ink);
  }
</style>
</head>
<body>
<main class="canvas">
  <section class="card card--front" aria-label="Card front">
    <div class="front-wordmark"><span class="mark-square"></span>LUMAR</div>
  </section>

  <section class="card card--back" aria-label="Card back">
    <span class="name-tab"></span>
    <div class="person">
      <h1 class="person-name">DANIEL CORVEY</h1>
      <p class="person-title">President</p>
    </div>

    <div class="brand"><span class="mark-square"></span>LUMAR</div>

    <address class="address">1842 Harlow Ridge NE<br>Atlanta, GA 30309</address>

    <ul class="contacts">
      <li>
        <svg viewBox="0 0 24 24" aria-hidden="true"><path d="M6.6 10.8a15.1 15.1 0 0 0 6.6 6.6l2.2-2.2c.3-.3.7-.4 1-.2 1.1.4 2.3.6 3.6.6.6 0 1 .4 1 1V20c0 .6-.4 1-1 1A17 17 0 0 1 3 4c0-.6.4-1 1-1h3.5c.6 0 1 .4 1 1 0 1.3.2 2.5.6 3.6.1.3 0 .7-.2 1z"/></svg>
        404-555-0187
      </li>
      <li>
        <svg viewBox="0 0 24 24" aria-hidden="true"><path d="M2 6h20v12H2z M2 6l10 7 10-7" stroke="#fff" stroke-width="1.5"/></svg>
        info@lumardevelopment.com
      </li>
      <li>
        <svg viewBox="0 0 24 24" aria-hidden="true"><circle cx="12" cy="12" r="10"/><path d="M2 12h20M12 2c3 3 3 17 0 20M12 2c-3 3-3 17 0 20" stroke="#fff" stroke-width="1.4" fill="none"/></svg>
        www.lumardevelopment.com
      </li>
    </ul>
  </section>
</main>
</body>
</html>
```